Email Template for AI Website Builder Marketing Campaign

Update: All the designs submitted have too much content for an email template. I have attached a mockup example of a simplified design. Please follow this guideline to revise your design to be less "wordy" and have less content to optimize the delivery rate of the emails. I have also attached the images I used to create the mockup. Feel free to use these images for your revised designs.
Original Brief:
I need a catchy email template for my new AI Website Builder, WebQuilt.ai. The template must be professional, colorful, yet not too complex. The concept of the product is this:
WebQuilt uses Artificial Intelligence (AI) to instantly build stunning websites, absolutely FREE. The user simply specifies their business name and business category (industry), and their stunning new website appears before their eyes!
The template will be used in MailChimp, so please provide the code that I can simply paste into the email body.
Here is a screenshot of our new website (which is not online yet) so you can match the color scheme and style of the email template to the new website design:
https://pixbinstore.com/art_img/7310582/2208634/48165027/9qrt41hwk826zlmpb3nqd7wyex_image.jpg
Let me know if you have any questions.
Thanks!
All submitted designs are too lengthy (too much content) for an email template. I will provide a mockup showing a sample of how you can simplify your design to function better as an email template and better suit my needs. I appreciate your patience!

```html
<!DOCTYPE html>
<html lang="en">
<head>
<meta charset="utf-8">
<title>WebQuilt – Build a website with AI</title>
<link rel="stylesheet" href="https://fonts.googleapis.com/css2?family=Arimo:ital,wght@0,400;0,600;0,700;1,400&family=Playfair+Display:wght@700;800&family=Poppins:wght@600&family=Open+Sans:wght@400&family=Exo+2:wght@600;700&display=swap">
<style>
:root{
  --ink:#111;
  --muted:#333;
  --white:#fff;
  --navy:#020b24;
  --cyan:#5bc8ec;
  --hero-text:#a6ecf7;
  --purple:#6b3fd6;
  --brand-dot:#3a8ce0;
}
*{box-sizing:border-box;margin:0;padding:0}
html,body{width:1200px;height:3424px;overflow:hidden;background:var(--white)}
body{position:relative;font-family:"Arimo",Arial,sans-serif;color:var(--ink)}
.abs{position:absolute}

/* header */
.brand{left:0;top:0;width:1200px;height:148px;display:flex;align-items:center;justify-content:center;gap:22px}
.brand-dot{width:70px;height:70px;border-radius:50%;background:var(--brand-dot)}
.brand-name{font-family:"Poppins",sans-serif;font-weight:600;font-size:64px;color:var(--ink);letter-spacing:-0.5px}

/* hero */
.hero{left:3px;top:150px;width:1194px;height:474px;background:linear-gradient(90deg,#4a2fb8 0%,#5a36c9 45%,#3b24a8 100%)}
.hero-art{left:620px;top:150px;width:420px;height:474px;background:radial-gradient(ellipse at 55% 45%,rgba(120,220,240,.35),rgba(60,40,170,0) 65%)}
.hero-copy{left:132px;top:342px;font-family:"Exo 2",sans-serif;color:var(--hero-text);font-weight:600}
.hero-copy .big{font-size:60px;font-weight:700;line-height:66px}
.hero-copy .line{font-size:30px;line-height:38px}

/* intro band */
.intro{left:3px;top:624px;width:1194px;height:250px;background:var(--navy);color:var(--white);text-align:center}
.intro h2{position:absolute;left:0;right:0;top:60px;font-family:"Playfair Display",serif;font-weight:700;font-size:46px}
.intro p{position:absolute;left:40px;right:40px;top:127px;font-size:28px;line-height:43px}

/* feature rows */
.title{font-family:"Playfair Display",serif;font-weight:800;color:var(--ink)}
.free-title{left:48px;top:925px;font-size:59px}
.copy{font-size:29.5px;line-height:43px;color:var(--ink)}
.free-copy{left:48px;top:1000px;width:500px}
.btn{display:flex;align-items:center;justify-content:center;background:var(--cyan);color:var(--ink)}
.free-btn{left:36px;top:1220px;width:257px;height:97px;font-size:28px}
.photo-puzzle{left:629px;top:920px;width:531px;height:440px;background:linear-gradient(120deg,#3a2a1c 0%,#8a6a48 45%,#b07a4c 70%,#2a1c14 100%)}
.photo-hand{left:35px;top:1447px;width:533px;height:546px;background:linear-gradient(135deg,#4c5548 0%,#1f3530 50%,#0c1f1e 100%)}
.ai-title{left:645px;top:1490px;font-size:63px;line-height:86px}
.ai-copy{left:645px;top:1700px;width:510px}

/* banner */
.banner{left:3px;top:2057px;width:1194px;height:313px;background:linear-gradient(90deg,#4a2466 0%,#2c2f86 50%,#0f58a8 100%)}
.banner-title{left:89px;top:2148px;font-family:"Open Sans",sans-serif;font-size:43px;color:var(--white)}
.banner-btn{left:97px;top:2258px;width:301px;height:51px;font-size:30px}

/* perks */
.perk{width:330px;text-align:center}
.perk svg{display:block;margin:0 auto}
.perk p{font-size:23px;line-height:44px;color:var(--ink);margin-top:8px}
.perk-device{left:36px;top:2448px}
.perk-media{left:436px;top:2456px}
.perk-cloud{left:834px;top:2452px}

/* call to action */
.cta{left:400px;top:2745px;width:344px;height:99px;font-weight:700;font-size:28px;letter-spacing:.3px}

/* social */
.social{left:377px;top:2924px;display:flex;gap:88px}
.social span{width:72px;height:72px;border:3px solid var(--ink);border-radius:50%}

/* footer */
.footer{left:0;top:3060px;width:1200px;text-align:center;font-size:21px;color:var(--muted);line-height:44px}
.footer .em{font-style:italic}
.footer .gap{margin-top:42px}
.footer a{color:#2a4a8a}
</style>
</head>
<body>

<header class="abs brand">
  <span class="brand-dot"></span>
  <span class="brand-name">WebQuilt</span>
</header>

<section class="abs hero" role="img" aria-label="Purple digital backdrop with an outlined AI head profile"></section>
<div class="abs hero-art"></div>
<div class="abs hero-copy">
  <div class="big">WebQuilt</div>
  <div class="line">uses Artificial Intelligence (AI)</div>
  <div class="line">to instantly build stunning</div>
  <div class="big">websites</div>
</div>

<section class="abs intro">
  <h2>It's time to ...</h2>
  <p>The user simply specifies their business name and business category (industry), and their stunning new website appears before their eyes!</p>
</section>

<h2 class="abs title free-title">Absolutely FREE</h2>
<p class="abs copy free-copy">It'll take minutes or less! A few simple steps will take you through image selection, content generation, color scheme, and layout!</p>
<a class="abs btn free-btn">Learn more</a>
<div class="abs photo-puzzle" role="img" aria-label="Photo of a child's portrait assembled from puzzle pieces"></div>

<div class="abs photo-hand" role="img" aria-label="Photo of a robotic hand touching a glowing surface"></div>
<h2 class="abs title ai-title">Build a website<br>with AI.</h2>
<p class="abs copy ai-copy">The system gathers some input: company name, business type, location, and color scheme, and the AI gathers text and images to build a professional site!</p>

<section class="abs banner" role="img" aria-label="Circuit-line backdrop in purple and blue"></section>
<h3 class="abs banner-title">Build a website with AI.</h3>
<a class="abs btn banner-btn">Learn more</a>

<div class="abs perk perk-device">
  <svg width="44" height="62" viewBox="0 0 44 62" fill="none" stroke="var(--purple)" stroke-width="4"><rect x="3" y="3" width="38" height="56" rx="6"/><circle cx="22" cy="50" r="2" fill="var(--purple)"/></svg>
  <p>Your site will fit perfectly into<br>a phone or tablet!</p>
</div>
<div class="abs perk perk-media">
  <svg width="62" height="50" viewBox="0 0 62 50" fill="none" stroke="var(--purple)" stroke-width="4"><path d="M4 14h12l5-8h20l5 8h12v32H4z"/><circle cx="31" cy="29" r="10"/></svg>
  <p>Customize your page with an<br>image, video, animation, or<br>anything else!</p>
</div>
<div class="abs perk perk-cloud">
  <svg width="62" height="62" viewBox="0 0 62 62" fill="none" stroke="var(--purple)" stroke-width="4"><path d="M31 4l7 6 9-1 2 9 8 5-4 8 4 8-8 5-2 9-9-1-7 6-7-6-9 1-2-9-8-5 4-8-4-8 8-5 2-9 9 1z"/><path d="M22 31l6 6 12-12"/></svg>
  <p>All sites run in a secure, high-<br>powered cloud computing<br>environment!</p>
</div>

<a class="abs btn cta">GENERATE NOW</a>

<div class="abs social" aria-label="Social links">
  <span></span><span></span><span></span>
</div>

<footer class="abs footer">
  <div class="em">Copyright (C) *|CURRENT_YEAR|* *|LIST:COMPANY|*. All rights reserved.</div>
  <div>*|IFNOT:ARCHIVE_PAGE|**|LIST:DESCRIPTION|**|END:IF|*</div>
  <div class="gap">Our mailing address is:</div>
  <div>*|IFNOT:ARCHIVE_PAGE|**|HTML:LIST_ADDRESS|**|END:IF|*</div>
  <div class="gap">Want to change how you receive these emails?</div>
  <div>You can <a>update your preferences</a> or <a>unsubscribe</a></div>
</footer>

</body>
</html>
```